Looking for a high-end business card design for a construction company

We are looking to update our business card design. We are a post-frame construction company that builds custom buildings, commercial spaces, homes, and anything else. We have multiple people working here so we would need something we can easily customize the information for the specific person. We need a name, website, cell phone, office phone as well as social icons. Our colors are black, white, and grey/silver so I would love a black background or something that is more striking than just a traditional white business card. Looking for something that is very professional with a high-end look/feel. I have attached our logos, they can be silver, white, grey, or black.
Industry/Entity Type
Construction
Contact Information for Business Card
Business logo, Name, Cell phone, Office phone, website, social Icons
Colors
Designer to choose only greyscale colors for use in the design.
Look and feel

```html
<!DOCTYPE html>
<html lang="en">
<head>
<meta charset="utf-8">
<title>Harlow Builders, Inc. – Business Card</title>
<link href="https://fonts.googleapis.com/css2?family=Montserrat:wght@300;400;600;800&display=swap" rel="stylesheet">
<style>
  :root {
    --stage: #e6e9ec;
    --card-white: #ffffff;
    --ink: #000000;
    --silver: #bdbdbd;
    --stripe-light: #f7f7f7;
    --stripe-soft: #ececec;
    --text-on-dark: #ffffff;
    --shadow: rgba(0, 0, 0, 0.28);
  }
  * { box-sizing: border-box; margin: 0; padding: 0; }
  html, body {
    width: 1200px;
    height: 900px;
    overflow: hidden;
    background: var(--stage);
    font-family: "Montserrat", sans-serif;
  }
  .stage {
    position: relative;
    width: 1200px;
    height: 900px;
  }
  .card {
    position: absolute;
    left: 250px;
    width: 700px;
    height: 400px;
    background: var(--card-white);
    box-shadow: 0 10px 24px var(--shadow);
    overflow: hidden;
  }
  .card--front { top: 40px; }
  .card--back { top: 470px; }

  /* Front */
  .front-texture {
    position: absolute;
    inset: 0 0 128px 0;
    background: linear-gradient(160deg, var(--stripe-light), var(--stripe-soft) 55%, var(--stripe-light));
  }
  .front-band {
    position: absolute;
    left: 0; right: 0; bottom: 0;
    height: 128px;
    background: var(--ink);
  }
  .wordmark {
    color: var(--ink);
    font-weight: 800;
    text-transform: uppercase;
    line-height: 1;
  }
  .wordmark__main { display: block; letter-spacing: 0.14em; }
  .wordmark__sub { display: block; letter-spacing: 0.2em; }
  .front-brand {
    position: absolute;
    top: 70px;
    left: 0; right: 0;
    text-align: center;
  }
  .front-brand .wordmark__main { font-size: 58px; }
  .front-brand .wordmark__sub { font-size: 22px; margin-top: 10px; }
  .front-web {
    position: absolute;
    top: 218px;
    left: 0; right: 0;
    display: flex;
    justify-content: center;
    align-items: center;
    gap: 12px;
    font-size: 13px;
    letter-spacing: 0.06em;
    color: var(--ink);
  }
  .front-web svg { width: 20px; height: 20px; }

  /* Back */
  .back-strip {
    position: absolute;
    left: 0; right: 0; top: 0;
    height: 20px;
    background: var(--silver);
  }
  .back-band {
    position: absolute;
    left: 0; right: 0; top: 20px;
    height: 120px;
    background: var(--ink);
  }
  .person {
    position: absolute;
    left: 46px;
    top: 58px;
    color: var(--text-on-dark);
  }
  .person__name {
    font-size: 30px;
    letter-spacing: 0.02em;
    font-weight: 300;
    line-height: 1.1;
  }
  .person__name strong { font-weight: 600; }
  .person__role {
    font-size: 15px;
    font-weight: 300;
    letter-spacing: 0.04em;
    margin-top: 2px;
  }
  .contacts {
    position: absolute;
    left: 46px;
    top: 162px;
    list-style: none;
  }
  .contact {
    display: flex;
    align-items: center;
    gap: 16px;
    height: 44px;
    font-size: 16px;
    color: var(--ink);
  }
  .contact__icon {
    width: 32px; height: 32px;
    border-radius: 50%;
    background: var(--ink);
    display: flex;
    align-items: center;
    justify-content: center;
    flex: none;
  }
  .contact__icon svg { width: 18px; height: 18px; }
  .social {
    display: flex;
    align-items: center;
    gap: 10px;
    margin-top: 6px;
    font-size: 14px;
    color: var(--ink);
  }
  .social__dot {
    width: 24px; height: 24px;
    border-radius: 50%;
    background: var(--ink);
    flex: none;
  }
  .social__label { margin-left: 8px; }
  .back-brand {
    position: absolute;
    right: 42px;
    top: 196px;
    text-align: center;
  }
  .back-brand .wordmark__main { font-size: 44px; }
  .back-brand .wordmark__sub { font-size: 17px; margin-top: 8px; }
</style>
</head>
<body>
<main class="stage">

  <section class="card card--front" aria-label="Business card front">
    <div class="front-texture" role="img" aria-label="Fine diagonal pinstripe texture in light grey"></div>
    <div class="front-brand wordmark">
      <span class="wordmark__main">Harlow</span>
      <span class="wordmark__sub">Builders, Inc.</span>
    </div>
    <div class="front-web">
      <svg viewBox="0 0 24 24" fill="none" stroke="#000" stroke-width="1.6" aria-hidden="true">
        <circle cx="12" cy="12" r="10"/>
        <ellipse cx="12" cy="12" rx="4.5" ry="10"/>
        <line x1="2" y1="12" x2="22" y2="12"/>
      </svg>
      <span>WWW.YOURWEBSITE.COM</span>
    </div>
    <div class="front-band"></div>
  </section>

  <section class="card card--back" aria-label="Business card back">
    <div class="back-strip"></div>
    <div class="back-band"></div>
    <div class="person">
      <p class="person__name"><strong>YOUR</strong> NAME</p>
      <p class="person__role">OCCUPATION</p>
    </div>

    <ul class="contacts">
      <li class="contact">
        <span class="contact__icon">
          <svg viewBox="0 0 24 24" fill="none" stroke="#fff" stroke-width="2" aria-hidden="true">
            <rect x="7" y="2.5" width="10" height="19" rx="2"/>
            <line x1="11" y1="18" x2="13" y2="18"/>
          </svg>
        </span>
        <span>0 123 000 4568</span>
      </li>
      <li class="contact">
        <span class="contact__icon">
          <svg viewBox="0 0 24 24" fill="#fff" aria-hidden="true">
            <path d="M3 8c0-2 3-3.5 9-3.5S21 6 21 8v2h-4V8.5c-1.2-.4-3-.6-5-.6s-3.8.2-5 .6V10H3z"/>
            <rect x="5" y="11" width="14" height="9" rx="1.5"/>
            <circle cx="12" cy="15.5" r="2.2" fill="#000"/>
          </svg>
        </span>
        <span>0 123 000 4568</span>
      </li>
      <li class="contact">
        <span class="contact__icon">
          <svg viewBox="0 0 24 24" fill="none" stroke="#fff" stroke-width="1.6" aria-hidden="true">
            <circle cx="12" cy="12" r="9"/>
            <ellipse cx="12" cy="12" rx="4" ry="9"/>
            <line x1="3" y1="12" x2="21" y2="12"/>
          </svg>
        </span>
        <span>www.yourwebsite.com</span>
      </li>
      <li class="social">
        <span class="social__dot"></span>
        <span class="social__dot"></span>
        <span class="social__dot"></span>
        <span class="social__label">social media name</span>
      </li>
    </ul>

    <div class="back-brand wordmark">
      <span class="wordmark__main">Harlow</span>
      <span class="wordmark__sub">Builders, Inc.</span>
    </div>
  </section>

</main>
</body>
</html>
```